Real Estate Biz Card

-Card Size: Standard
-Background: Dark grey or black. I am open to gradient or a textured background.
-Other Colors: I dont mind pops of color. Contrasty blue, lime green, red Etc. Feel free to get creative.
-Text color: be creative
-Font: I like modern styles. Something that works well with my KV718 logo. See attached
-I would like my logo (KV718) watermarked on the card. Either on one side or both.
-Front of Card: keep it simple. Head shot, name, Logo, Phone #
-Back: add the rest of the details. See list below.
-brokerages logo as well as the Domivest and Equal Housing Opportunity logos on the card
-Name: Tod Marwick
-Residential Real Estate
-Cell:
-Email:
-Site:
-Office Address:
-very small/fine print "Each office independently owned & operated

```html
<!DOCTYPE html>
<html lang="en">
<head>
<meta charset="utf-8">
<title>KV718 Business Card – Tod Marwick</title>
<link href="https://fonts.googleapis.com/css2?family=Montserrat:ital,wght@0,300;0,400;0,500;0,600;0,700;0,800;1,400&family=Raleway:wght@300;400&display=swap" rel="stylesheet">
<style>
  :root {
    --page-bg: #1f1f1f;
    --card-top: #4a4a4c;
    --card-bottom: #2b2b2d;
    --ink: #ffffff;
    --ink-soft: #d9d9d9;
    --accent-blue: #2f6fd0;
    --accent-red: #d0242b;
    --photo-a: #6c7a8c;
    --photo-b: #3d5f95;
  }
  * { box-sizing: border-box; margin: 0; padding: 0; }
  html, body { width: 1200px; height: 535px; overflow: hidden; }
  body {
    background: var(--page-bg);
    font-family: "Montserrat", sans-serif;
    color: var(--ink);
    position: relative;
  }
  .card {
    position: absolute;
    top: 119px;
    width: 520px;
    height: 297px;
    overflow: hidden;
    background: linear-gradient(160deg, var(--card-top) 0%, var(--card-bottom) 75%);
    box-shadow: 0 6px 18px rgba(0,0,0,.45);
  }
  .card--front { left: 60px; }
  .card--back { left: 620px; }

  .brand-name {
    position: absolute;
    font-family: "Montserrat", sans-serif;
    font-weight: 500;
    color: var(--ink);
    line-height: 1;
    letter-spacing: 3px;
  }
  .card--front .brand-name { left: 76px; top: 52px; font-size: 56px; }
  .card--back .brand-name { left: 0; right: 0; top: 48px; text-align: center; font-size: 92px; }

  .rule { position: absolute; height: 2px; }
  .rule--blue { background: var(--accent-blue); }
  .rule--red { background: var(--accent-red); }
  .card--front .rule--blue { left: 0; top: 129px; width: 300px; }
  .card--front .rule--red { left: 150px; top: 222px; width: 160px; }
  .card--back .rule--blue { left: 71px; top: 169px; width: 380px; }

  .monogram {
    position: absolute;
    left: 20px;
    top: 150px;
    font-size: 72px;
    font-weight: 800;
    letter-spacing: -6px;
    line-height: 1;
  }
  .agent-name {
    position: absolute;
    left: 150px;
    font-family: "Raleway", sans-serif;
    font-weight: 300;
    font-size: 26px;
    letter-spacing: 6px;
    line-height: 1;
  }
  .agent-name--first { top: 158px; }
  .agent-name--last { top: 190px; }
  .agent-phone {
    position: absolute;
    left: 150px;
    top: 228px;
    font-weight: 300;
    font-size: 17px;
    letter-spacing: 1px;
    line-height: 1;
  }
  .agent-title {
    position: absolute;
    left: 150px;
    top: 253px;
    font-weight: 700;
    font-size: 12px;
    letter-spacing: .5px;
    line-height: 1;
  }
  .headshot {
    position: absolute;
    right: 0;
    top: 0;
    width: 202px;
    height: 297px;
    background: linear-gradient(180deg, var(--photo-a) 0%, var(--photo-b) 70%);
  }

  .contact-row {
    position: absolute;
    left: 0; right: 0;
    top: 203px;
    display: flex;
    justify-content: center;
    gap: 22px;
    font-size: 12px;
    letter-spacing: 1px;
  }
  .contact-item { display: flex; align-items: center; gap: 7px; }
  .contact-item svg { width: 18px; height: 18px; fill: none; stroke: var(--ink); stroke-width: 1.6; }

  .fine-print {
    position: absolute;
    left: 30px;
    width: 190px;
    top: 250px;
    font-style: italic;
    font-size: 11px;
    line-height: 1.35;
    text-align: center;
    color: var(--ink-soft);
  }
  .brokerage {
    position: absolute;
    left: 243px;
    top: 252px;
    width: 140px;
    font-size: 13px;
    font-weight: 600;
    line-height: 1.2;
    letter-spacing: .5px;
  }
  .badge {
    position: absolute;
    top: 252px;
    width: 28px;
    height: 28px;
    background: var(--ink);
  }
  .badge--housing { left: 396px; }
  .badge--association { left: 452px; }
</style>
</head>
<body>

  <section class="card card--front" aria-label="Card front">
    <div class="brand-name">KV718</div>
    <div class="rule rule--blue"></div>
    <div class="monogram">TM</div>
    <div class="agent-name agent-name--first">OD</div>
    <div class="agent-name agent-name--last">ARWICK</div>
    <div class="rule rule--red"></div>
    <div class="agent-phone">555 014 7382</div>
    <div class="agent-title">REAL ESTATE BROKER</div>
    <div class="headshot" role="img" aria-label="Head shot of Tod Marwick in a blue shirt"></div>
  </section>

  <section class="card card--back" aria-label="Card back">
    <div class="brand-name">KV718</div>
    <div class="rule rule--blue"></div>

    <div class="contact-row">
      <div class="contact-item">
        <svg viewBox="0 0 18 18" aria-hidden="true"><rect x="5" y="1.5" width="8" height="15" rx="1.5"/><line x1="8" y1="14" x2="10" y2="14"/></svg>
        <span>XXXXXXXX</span>
      </div>
      <div class="contact-item">
        <svg viewBox="0 0 18 18" aria-hidden="true"><rect x="1.5" y="4" width="15" height="10"/><polyline points="1.5,4 9,10 16.5,4"/></svg>
        <span>XXXXXXXX</span>
      </div>
      <div class="contact-item">
        <svg viewBox="0 0 18 18" aria-hidden="true"><circle cx="9" cy="9" r="7.5"/><ellipse cx="9" cy="9" rx="3.2" ry="7.5"/><line x1="1.5" y1="9" x2="16.5" y2="9"/></svg>
        <span>XXXXX.COM</span>
      </div>
      <div class="contact-item">
        <svg viewBox="0 0 18 18" aria-hidden="true"><circle cx="9" cy="9" r="7.5"/><path d="M9 13.5c-2-2.4-3-4-3-5.3a3 3 0 0 1 6 0c0 1.3-1 2.9-3 5.3z"/></svg>
        <span>XXXXXXXX</span>
      </div>
    </div>

    <p class="fine-print">"Each Office Independently<br>Owned &amp; Operated"</p>
    <div class="brokerage">HARBORLINE EASTSIDE</div>
    <div class="badge badge--housing" aria-label="Equal housing badge"></div>
    <div class="badge badge--association" aria-label="Domivest badge"></div>
  </section>

</body>
</html>
```